Brenvick Holdings LLC, new Business cards

I'm moving offices and need new cards. Plus I'm open to modifying the current design of my card. I will keep the logo but would like to explore other layouts and fonts for the design. I've included the current double sided card for reference. I Like the navy color and white. Might be open to grays or silver. Needs to be clean and elegant.

Target Market(s)

Investors, buyers & sellers of private equities and real estate.

Contact Information for Business Card

Brenvick Holdings
Dorian P.K. Halvers, Managing Principal
418 Ostrander Ave., Suite 612
Denver, CO 80319
M: 970-555-0147, O: 303-555-0192
Dorian@brenvickholdings.example
Brenvickholdings.example

Colors
0354a2
ffffff
c4c4c4

Requirements
Must have
• Business card details.
• Logo raised or embossed, it was designed after a wax seal. Current has raised ink.
Nice to have
• Space on card to write additional notes.

```html
<!DOCTYPE html>
<html lang="en">
<head>
<meta charset="utf-8">
<title>Brenvick Holdings – Business Card</title>
<link href="https://fonts.googleapis.com/css2?family=Montserrat:wght@800&family=Libre+Baskerville:wght@700&family=Roboto:wght@400;500&display=swap" rel="stylesheet">
<style>
  :root {
    --navy: #24236b;
    --white: #ffffff;
    --stage: #e6e7eb;
    --shadow: rgba(20, 20, 50, 0.18);
  }
  * { box-sizing: border-box; margin: 0; padding: 0; }
  html, body { width: 1200px; height: 900px; overflow: hidden; }
  body {
    background: var(--stage);
    font-family: "Roboto", Arial, sans-serif;
    color: var(--navy);
    position: relative;
  }
  .card {
    position: absolute;
    left: 285px;
    width: 630px;
    height: 360px;
    background: var(--white);
    border-radius: 26px;
    overflow: hidden;
    box-shadow: 0 10px 30px var(--shadow);
  }
  .card--notes { top: 70px; }
  .card--details { top: 470px; }

  /* Notes side */
  .notes-band {
    position: absolute; left: 0; top: 0; width: 100%; height: 82px;
    background: var(--navy);
  }
  .notes-brand {
    position: absolute; left: 220px; top: 22px;
    display: flex; align-items: center; gap: 14px;
  }
  .notes-brand .seal-spot {
    width: 38px; height: 38px; border-radius: 50%;
    background: var(--white);
  }
  .notes-brand .brand-name {
    font-family: "Roboto", Arial, sans-serif;
    font-weight: 500; font-size: 26px; letter-spacing: 3px;
    color: var(--white); text-transform: uppercase;
  }
  .note-label {
    position: absolute; left: 40px; top: 128px;
    display: flex; align-items: center; gap: 8px;
    font-family: "Montserrat", Arial, sans-serif;
    font-weight: 800; font-size: 13px; letter-spacing: 1px;
  }

  /* Details side */
  .holder {
    position: absolute; left: 40px; top: 72px;
  }
  .holder-name {
    font-family: "Montserrat", Arial, sans-serif;
    font-weight: 800; font-size: 19px; letter-spacing: 0.5px;
    text-transform: uppercase;
  }
  .holder-title {
    font-family: "Libre Baskerville", Georgia, serif;
    font-weight: 700; font-size: 14px; margin-top: 2px;
  }
  .contact-row {
    display: flex; align-items: flex-start; gap: 12px;
    font-size: 15px; line-height: 1.3;
  }
  .contact-row svg { flex: none; margin-top: 2px; }
  .address { margin-top: 14px; }
  .contact-list {
    position: absolute; left: 40px; bottom: 40px;
    display: flex; flex-direction: column; gap: 6px;
  }
  .contact-list .contact-row { font-size: 17px; }
  .brand-mark {
    position: absolute; right: 34px; top: 50px; width: 250px;
    display: flex; flex-direction: column; align-items: center; gap: 18px;
  }
  .brand-mark .seal-spot {
    width: 170px; height: 170px; border-radius: 50%;
    background: var(--navy);
  }
  .brand-mark .brand-name {
    font-family: "Roboto", Arial, sans-serif;
    font-weight: 500; font-size: 24px; letter-spacing: 3px;
    text-transform: uppercase; text-align: center;
  }
</style>
</head>
<body>

<section class="card card--notes" aria-label="Card notes side">
  <div class="notes-band"></div>
  <div class="notes-brand">
    <span class="seal-spot"></span>
    <span class="brand-name">Brenvick Holdings</span>
  </div>
  <div class="note-label">
    <svg width="18" height="16" viewBox="0 0 18 16" aria-hidden="true">
      <rect x="1" y="3" width="12" height="12" rx="2" fill="none" stroke="currentColor" stroke-width="2"/>
      <path d="M6 10 L15 1 L17 3 L8 12 L5 13 Z" fill="currentColor"/>
    </svg>
    NOTE
  </div>
</section>

<section class="card card--details" aria-label="Card details side">
  <div class="holder">
    <h1 class="holder-name">Dorian P.K. Halvers</h1>
    <p class="holder-title">Managing Principal</p>
    <div class="contact-row address">
      <svg width="12" height="16" viewBox="0 0 12 16" aria-hidden="true">
        <path d="M6 0 C2.7 0 0 2.6 0 5.9 C0 10 6 16 6 16 S12 10 12 5.9 C12 2.6 9.3 0 6 0 Z M6 8.3 A2.4 2.4 0 1 1 6 3.5 A2.4 2.4 0 0 1 6 8.3 Z" fill="currentColor"/>
      </svg>
      <span>418 Ostrander Ave., Suite 612<br>Denver, CO 80319</span>
    </div>
  </div>

  <div class="contact-list">
    <div class="contact-row">
      <svg width="16" height="16" viewBox="0 0 16 16" aria-hidden="true">
        <path d="M3.5 1 L6 4 L4.6 5.8 C5.5 7.8 8 10.4 10.2 11.4 L12 10 L15 12.5 L13.4 14.8 C8 14.8 1.2 8 1.2 2.6 Z" fill="currentColor"/>
      </svg>
      <span>M: 970-555-0147, O: TBD</span>
    </div>
    <div class="contact-row">
      <svg width="18" height="14" viewBox="0 0 18 14" aria-hidden="true">
        <rect x="0" y="0" width="18" height="14" rx="1.5" fill="currentColor"/>
        <path d="M1 1.5 L9 8 L17 1.5" fill="none" stroke="#fff" stroke-width="1.4"/>
      </svg>
      <span>Dorian@brenvickholdings.example</span>
    </div>
    <div class="contact-row">
      <svg width="18" height="18" viewBox="0 0 18 18" aria-hidden="true">
        <g fill="none" stroke="currentColor" stroke-width="1.5">
          <circle cx="9" cy="9" r="8"/>
          <ellipse cx="9" cy="9" rx="3.5" ry="8"/>
          <path d="M1 9 H17 M2.5 5 H15.5 M2.5 13 H15.5"/>
        </g>
      </svg>
      <span>Brenvickholdings.example</span>
    </div>
  </div>

  <div class="brand-mark">
    <span class="seal-spot"></span>
    <span class="brand-name">Brenvick Holdings</span>
  </div>
</section>

</body>
</html>
```